Signage Design Project

We need a logo and signage for the shopfront of a personal fitness training gym and coaching facility. We want the signage to cover the glass shopfront windows which consist of 4 glass windows with dimensions: 1 of 200cm x 180cm, 2 of 180cm x 135cm and 1 of 180cm x 180cm. The windows that are 200x 180 and 180x180 are the most visable/ important. We want the 200x180 to display the logo and our name which is "Harborline Fitness Centre" with further information of: Your personal training studio and boutique coaching gym Ph: 9471 2286.
For the window with 180 x 180cm measurement we want to list the services we provide which are:
Personal Training Sessions | Group Classes|Weight Loss |Toning & Sculpting|Bodybuilding I Cardio|Weights| Kettlebells| Boxing| Circuits I Team Building Programs| Boot Camp I Healthy Lifestyle & Wellness Coaching
The 2 windows 180x135cm are diagonal to the entry of the shop. We want them to be the same and plainer in design with the words: Harborline Fitness Centre
Personal Training Studio and Boutique Coaching Gym
The signage design also includes an acrylic window box that lights up which is to display the logo and Harborline Fitness Centre

```html
<!DOCTYPE html>
<html lang="en">
<head>
<meta charset="utf-8">
<title>Harborline Fitness Centre – Window Signage</title>
<link rel="stylesheet" href="https://fonts.googleapis.com/css2?family=Arimo:wght@700&family=Francois+One&family=Orbitron:wght@500&display=swap">
<style>
  :root {
    --canvas: #ffffff;
    --orange: #f58220;
    --orange-soft: #f9a35c;
    --cream: #fffaf4;
    --navy: #1f3a93;
    --line-blue: #2a3f8f;
    --brand-blue: #1b7fd1;
    --ink: #1a1a1a;
    --silhouette: rgba(58, 29, 12, 0.55);
    --silhouette-fade: rgba(58, 29, 12, 0.15);
    --white: #ffffff;
    --shadow: rgba(0, 0, 0, 0.35);
  }
  * { margin: 0; padding: 0; box-sizing: border-box; }
  html, body { width: 1200px; height: 848px; overflow: hidden; background: var(--canvas); }
  .canvas { position: relative; width: 1200px; height: 848px; }

  .panel {
    position: absolute;
    overflow: hidden;
    box-shadow: 3px 4px 6px var(--shadow);
  }
  .panel--gradient { background: linear-gradient(180deg, var(--orange) 0%, var(--orange-soft) 50%, var(--cream) 100%); }
  .panel--solid { background: var(--orange); }

  .panel--hero { left: 48px; top: 72px; width: 356px; height: 256px; transform: rotate(-2.8deg); }
  .panel--main { left: 438px; top: 218px; width: 342px; height: 306px; transform: rotate(4.8deg); }
  .panel--services { left: 808px; top: 406px; width: 344px; height: 340px; transform: rotate(-5deg); }

  .brand-name {
    font-family: "Arimo", Arial, sans-serif;
    font-weight: 700;
    color: var(--brand-blue);
    line-height: 1.08;
    text-align: center;
    padding: 12px 8px 0;
  }
  .panel--hero .brand-name { font-size: 30px; }
  .panel--main .brand-name { font-size: 29px; padding-top: 10px; }

  .activity-band {
    position: absolute; left: 4px; right: 4px;
    background: linear-gradient(90deg, var(--silhouette-fade), var(--silhouette) 15%, var(--silhouette) 85%, var(--silhouette-fade));
    border-radius: 2px;
  }
  .activity-band::after {
    content: ""; position: absolute; left: 0; right: 0; top: 62%;
    height: 2px; background: var(--line-blue);
  }
  .panel--hero .activity-band { top: 104px; height: 64px; }
  .panel--main .activity-band { top: 90px; height: 70px; }
  .panel--services .activity-band { bottom: 8px; height: 62px; }
  .panel--services .activity-band::after { display: none; }

  .tagline {
    position: absolute; left: 0; right: 0;
    font-family: "Arimo", Arial, sans-serif;
    font-weight: 700;
    color: var(--navy);
    text-align: center;
    line-height: 1.25;
  }
  .panel--hero .tagline { top: 182px; font-size: 20px; }
  .panel--main .tagline { top: 166px; font-size: 20px; }

  .phone {
    position: absolute; left: 0; right: 0; bottom: 8px;
    font-family: "Orbitron", sans-serif;
    font-weight: 500;
    font-size: 26px;
    color: var(--ink);
    text-align: center;
    letter-spacing: 1px;
  }

  .services-title {
    font-family: "Arimo", Arial, sans-serif;
    font-weight: 700;
    font-size: 20px;
    color: var(--ink);
    text-align: center;
    line-height: 1.2;
    padding-top: 24px;
  }
  .service-columns {
    display: flex; gap: 10px;
    padding: 36px 10px 0 10px;
    font-family: "Francois One", sans-serif;
    font-size: 16px;
    color: var(--white);
    line-height: 1.4;
  }
  .service-list { list-style: none; flex: 1; }
  .service-list li::before { content: "•"; margin-right: 2px; }
  .service-list--right { margin-top: -22px; }
  .service-list .indent { padding-left: 10px; }
  .service-list .indent::before { content: ""; margin: 0; }
</style>
</head>
<body>
<main class="canvas">

  <section class="panel panel--gradient panel--hero">
    <h1 class="brand-name">Harborline Fitness Centre</h1>
    <div class="activity-band" role="img" aria-label="Row of athlete silhouettes along a blue line: weightlifter, footballer, cyclist, martial artist, basketballer and batter"></div>
    <p class="tagline">Your Personal Training Studio<br>and Boutique Coaching Gym</p>
  </section>

  <section class="panel panel--gradient panel--main">
    <h1 class="brand-name">Harborline Fitness Centre</h1>
    <div class="activity-band" role="img" aria-label="Row of athlete silhouettes along a blue line: weightlifter, footballer, cyclist, martial artist, basketballer and batter"></div>
    <p class="tagline">Your Personal Training Studio<br>and<br>Boutique Coaching Gym</p>
    <p class="phone">Ph: 02 9471 2286</p>
  </section>

  <section class="panel panel--solid panel--services">
    <h2 class="services-title">Personal Training Sessions<br>Group Classes</h2>
    <div class="service-columns">
      <ul class="service-list">
        <li>Weight Loss</li>
        <li>Toning &amp; Sculpting</li>
        <li>Bodybuilding</li>
        <li>Cardio</li>
        <li>Weights</li>
        <li>Kettlebells</li>
        <li>Boxing</li>
      </ul>
      <ul class="service-list service-list--right">
        <li>Circuits</li>
        <li>Team Building</li>
        <li class="indent">Programs</li>
        <li>Boot Camp</li>
        <li>Healthy Lifestyle &amp;</li>
        <li class="indent">Wellness Coaching</li>
      </ul>
    </div>
    <div class="activity-band" role="img" aria-label="Row of athlete silhouettes: weightlifter, footballer, cyclist, martial artist, basketballer and batter"></div>
  </section>

</main>
</body>
</html>
```